Business card - Harbourline Stoneworks

Design a business card utilizing the given logo.
colors we like: Black, greys, Teal, blues.
Tri color card, horizontal orientation likely
Logo and name likely best on top.
Info on card:

Dennis Farrowby
#5 - 4180 Maple Ridge Blvd.
Langford, B.C. V3K 2R9

778.555.0193
dennisfarrowby@brellnet.ca

Slogan: "Crafting Homes"

We are a construction company that specializes in new home construction on the West coast of BC Canada. Open Concepts designs of high end homes.

```html
<!DOCTYPE html>
<html lang="en">
<head>
<meta charset="utf-8">
<title>Harbourline Stoneworks – Business Card</title>
<link rel="stylesheet" href="https://fonts.googleapis.com/css2?family=Arimo:wght@400;700&display=swap">
<style>
  :root {
    --backdrop: #e4e4e4;
    --card: #ffffff;
    --ink: #111111;
    --ink-soft: #333333;
    --muted: #6b6b6b;
    --band-dark: #0b0b0b;
    --band-grey: #7a7a7a;
    --mark: #2a2a2a;
  }
  * { box-sizing: border-box; margin: 0; padding: 0; }
  html, body { width: 1200px; height: 1000px; overflow: hidden; }
  body {
    background: var(--backdrop);
    font-family: "Arimo", Arial, sans-serif;
    color: var(--ink);
    position: relative;
  }
  .card {
    position: absolute;
    left: 160px;
    top: 236px;
    width: 880px;
    height: 520px;
    background: var(--card);
    overflow: hidden;
    box-shadow: 0 6px 18px rgba(0,0,0,0.25);
  }
  .card__band {
    position: absolute;
    left: 0;
    top: 0;
    width: 880px;
    height: 520px;
  }
  .card__slogan {
    position: absolute;
    left: 56px;
    top: 280px;
    transform: translate(-50%, -50%) rotate(-90deg);
    white-space: nowrap;
    color: #ffffff;
    font-size: 28px;
    letter-spacing: 0.5px;
  }
  .brand {
    position: absolute;
    left: 236px;
    top: 78px;
    height: 94px;
    display: flex;
    align-items: center;
    gap: 24px;
    white-space: nowrap;
  }
  .brand__dot {
    width: 94px;
    height: 94px;
    border-radius: 50%;
    background: var(--mark);
    flex: none;
  }
  .brand__name {
    font-size: 32px;
    font-weight: 400;
    color: var(--mark);
    letter-spacing: 1px;
    text-transform: uppercase;
  }
  .contact {
    position: absolute;
    left: 348px;
    top: 232px;
  }
  .contact__name {
    font-size: 32px;
    font-weight: 700;
    line-height: 1.2;
  }
  .contact__role {
    font-size: 24px;
    color: var(--muted);
    line-height: 1.2;
    margin-top: 2px;
  }
  .contact__address {
    font-size: 26px;
    color: var(--ink-soft);
    line-height: 34px;
    margin-top: 34px;
  }
  .contact__lines {
    list-style: none;
    margin-top: 16px;
  }
  .contact__line {
    display: flex;
    align-items: center;
    gap: 12px;
    font-size: 26px;
    color: var(--ink-soft);
    line-height: 38px;
    white-space: nowrap;
  }
  .contact__icon {
    width: 20px;
    height: 20px;
    flex: none;
  }
</style>
</head>
<body>
  <div class="card">
    <svg class="card__band" viewBox="0 0 880 520" aria-hidden="true">
      <path d="M0 0 H128 C190 80 215 180 196 290 C182 380 166 450 172 520 H0 Z" fill="var(--band-grey)"/>
      <path d="M0 0 H108 C164 76 186 176 168 284 C154 370 134 440 136 520 H0 Z" fill="var(--band-dark)" stroke="#ffffff" stroke-width="6"/>
    </svg>
    <p class="card__slogan">Crafting Homes</p>

    <div class="brand">
      <span class="brand__dot"></span>
      <span class="brand__name">Harbourline Stoneworks</span>
    </div>

    <div class="contact">
      <h1 class="contact__name">Dennis Farrowby</h1>
      <p class="contact__role">CEO</p>
      <p class="contact__address">#5 - 4180 Maple Ridge Blvd.<br>Langford, B.C. V3K 2R9</p>
      <ul class="contact__lines">
        <li class="contact__line">
          <svg class="contact__icon" viewBox="0 0 22 22" aria-hidden="true">
            <rect x="2" y="6" width="18" height="14" rx="2" fill="var(--ink-soft)"/>
            <rect x="5" y="2" width="5" height="6" fill="var(--ink-soft)"/>
            <rect x="12" y="9" width="5" height="8" fill="#ffffff"/>
          </svg>
          778.555.0193
        </li>
        <li class="contact__line">
          <svg class="contact__icon" viewBox="0 0 22 22" aria-hidden="true">
            <rect x="2" y="5" width="18" height="12" fill="none" stroke="var(--ink-soft)" stroke-width="1.6"/>
            <path d="M2 5 L11 12 L20 5" fill="none" stroke="var(--ink-soft)" stroke-width="1.6"/>
          </svg>
          dennisfarrowby@brellnet.ca
        </li>
      </ul>
    </div>
  </div>
</body>
</html>
```